Modern Innovative Business Card Design

We require a nice, modern, clean business card design, ready for upload to Cardomora. Our company develops online banking software solutions for small financial insitutions. The design should be clean, professional, but yet not "corporate boring". See www.fyrolt.com for an idea of business image and profile. The design should communicate innovation, be modern and fresh, yet look professional and established.

Target Market(s)

Finance industry, bankers, entrepreneurs

Industry/Entity Type

Financial

Contact Information for Business Card

Tobias Wendlerup
CEO

FYROLT BV
Lindenwerf 38
1027 HX Amsterdam
The Netherlands

Phone: +31 20 517 8036
Direct: +31 20 604 1758
Skype: tobias.fyrolt
ceo@fyrolt.com
www.fyrolt.com

Font styles to use
Sans Serif

Requirements
Must have
• Should look clean, modern and professional. File should be ready for upload to cardomora.
Should not have
• Boring standard corporate layout

```html
<!DOCTYPE html>
<html lang="en">
<head>
<meta charset="UTF-8">
<title>FYROLT — Business Card</title>
<link href="https://fonts.googleapis.com/css2?family=Lato:wght@400;700&display=swap" rel="stylesheet">
<style>
  :root {
    --backdrop: #2a2a2c;
    --card: #ffffff;
    --green: #7cc242;
    --ink: #4a4a4a;
    --ink-soft: #5a5a5a;
    --chat-blue: #1fa9e6;
  }
  * { margin: 0; padding: 0; box-sizing: border-box; }
  html, body {
    width: 1200px; height: 800px; overflow: hidden;
    background: var(--backdrop);
    font-family: "Lato", sans-serif;
  }
  .card {
    position: absolute; left: 100px; top: 110px;
    width: 1000px; height: 580px;
    background: var(--card);
    box-shadow: 0 12px 40px rgba(0,0,0,.45);
    overflow: hidden;
  }
  .wordmark {
    position: absolute; left: 250px; top: 45px;
    font-size: 148px; font-weight: 700; letter-spacing: 6px;
    color: var(--ink); line-height: 1;
  }
  .holder { position: absolute; left: 400px; top: 222px; text-align: center; width: 300px; }
  .holder-name { color: var(--green); font-weight: 700; font-size: 26px; }
  .holder-role { color: var(--ink); font-size: 21px; margin-top: 2px; }
  .rule { position: absolute; height: 2px; background: var(--green); }
  .detail { position: absolute; color: var(--ink-soft); font-size: 21px; line-height: 28px; white-space: nowrap; }
  .icon-tile {
    position: absolute; width: 56px; height: 56px; background: var(--green);
    display: flex; align-items: center; justify-content: center;
  }
  .icon-tile svg { width: 30px; height: 30px; }
  .chat { position: absolute; left: 330px; top: 470px; width: 220px; text-align: center; }
  .chat-dot { display: block; width: 30px; height: 30px; border-radius: 50%; background: var(--chat-blue); margin: 0 auto 8px; }
  .chat-handle { color: var(--green); font-size: 23px; }
</style>
</head>
<body>
<main class="card">
  <div class="wordmark">FYROLT</div>

  <div class="holder">
    <div class="holder-name">Tobias Wendlerup</div>
    <div class="holder-role">CEO FYROLT BV</div>
  </div>

  <section class="contact-direct">
    <div class="rule" style="left:0;top:290px;width:560px"></div>
    <div class="detail" style="left:95px;top:300px">+31 20 517 8036<br>+31 20 604 1758</div>
    <div class="detail" style="left:95px;top:362px">ceo@fyrolt.com</div>
    <div class="rule" style="left:0;top:398px;width:560px"></div>
    <div class="icon-tile" style="left:504px;top:292px">
      <svg viewBox="0 0 32 32" fill="none" stroke="#fff" stroke-width="2.2" stroke-linejoin="round">
        <path d="M6 13c0-4 4-6 10-6s10 2 10 6l-4 1-1-3H11l-1 3z"/>
        <rect x="9" y="15" width="14" height="10" rx="1"/>
        <circle cx="16" cy="20" r="2.5"/>
      </svg>
    </div>
    <div class="icon-tile" style="left:504px;top:400px">
      <svg viewBox="0 0 32 32" fill="#fff">
        <path d="M4 9h24v14H4z"/>
        <path d="M4 9l12 9 12-9" fill="none" stroke="#7cc242" stroke-width="2"/>
      </svg>
    </div>
  </section>

  <section class="contact-office">
    <div class="rule" style="left:620px;top:400px;width:380px"></div>
    <div class="detail" style="left:630px;top:410px">Lindenwerf 38 1027 HX<br>Amsterdam The Netherlands</div>
    <div class="detail" style="left:630px;top:470px">www.fyrolt.com</div>
    <div class="rule" style="left:620px;top:505px;width:380px"></div>
    <div class="icon-tile" style="left:944px;top:447px">
      <svg viewBox="0 0 32 32" fill="#fff">
        <path d="M16 5L3 16h4v11h7v-7h4v7h7V16h4z"/>
      </svg>
    </div>
    <div class="icon-tile" style="left:944px;top:509px">
      <svg viewBox="0 0 32 32" fill="none" stroke="#fff" stroke-width="1.8">
        <circle cx="16" cy="16" r="11"/>
        <ellipse cx="16" cy="16" rx="5" ry="11"/>
        <path d="M5 16h22M7 10h18M7 22h18"/>
      </svg>
    </div>
  </section>

  <div class="chat">
    <span class="chat-dot"></span>
    <span class="chat-handle">tobias.fyrolt</span>
  </div>
</main>
</body>
</html>
```